Fashion Design Business Card

I need a new business card designed for a new fashion company. I have attached what I have currently designed. I want it more feminine looking, the logo needs to be gold. I want it simple, feminine and stylish. Please give me some different ideas with the fonts.
Updates

I need to send the design we currently have, as we have worked out the logo.
You also need all of our details
Industry/Entity Type
Fashion
Look and feel
Each slider illustrates characteristics of the customer's brand and the style your logo design should communicate.

```html
<!DOCTYPE html>
<html lang="en">
<head>
<meta charset="utf-8">
<title>Mirela Hartwood – Business Cards</title>
<link rel="stylesheet" href="https://fonts.googleapis.com/css2?family=Cinzel:wght@400&family=Open+Sans:wght@400&display=swap">
<style>
  :root {
    --stage: #000000;
    --card-white: #ffffff;
    --rose: #f08fac;
    --rose-deep: #ec7fa0;
    --rose-light: #fbe3ea;
    --sun: #ffe01a;
    --ink: #3a3a3a;
    --ink-soft: #555555;
    --serif: 'Cinzel', 'Times New Roman', serif;
    --sans: 'Open Sans', Arial, sans-serif;
  }
  * { margin: 0; padding: 0; box-sizing: border-box; }
  html, body { width: 1200px; height: 900px; overflow: hidden; background: var(--stage); }
  .sheet { position: relative; width: 1200px; height: 900px; }

  .card {
    position: absolute;
    width: 504px;
    height: 288px;
    border-radius: 9px;
    overflow: hidden;
  }
  .card--front { background: var(--card-white); left: 76px; }
  .card--back { left: 622px; }
  .row-top { top: 154px; }
  .row-bottom { top: 462px; }

  .card--back-rose {
    background: radial-gradient(ellipse 48% 62% at 50% 40%, #ffffff 0%, var(--rose-light) 30%, var(--rose) 75%, var(--rose-deep) 100%);
  }
  .card--back-sun { background: var(--sun); }

  .brand-ring { position: absolute; left: 50%; transform: translateX(-50%); display: block; }
  .card--front .brand-ring { top: 40px; }
  .card--back .brand-ring { top: 42px; }

  .brand-name {
    position: absolute;
    left: 0; right: 0;
    text-align: center;
    font-family: var(--serif);
    color: var(--ink);
    letter-spacing: 1.5px;
    word-spacing: 6px;
  }
  .card--front .brand-name { top: 142px; font-size: 21px; }
  .card--back .brand-name { top: 192px; font-size: 24px; }

  .accent-rule {
    position: absolute;
    top: 197px;
    left: 90px;
    width: 324px;
    height: 3px;
  }
  .accent-rule--rose { background: linear-gradient(90deg, transparent, var(--rose) 50%, transparent); }
  .accent-rule--sun { background: linear-gradient(90deg, transparent, var(--sun) 50%, transparent); }

  .holder { position: absolute; left: 28px; top: 218px; }
  .holder-name {
    font-family: var(--serif);
    font-size: 19px;
    color: var(--ink-soft);
    letter-spacing: 1px;
    word-spacing: 4px;
    line-height: 1;
  }
  .holder-role {
    font-family: var(--serif);
    font-size: 10.5px;
    color: var(--ink-soft);
    letter-spacing: 0.8px;
    margin-top: 6px;
  }

  .contact {
    position: absolute;
    left: 268px;
    top: 214px;
    font-family: var(--sans);
    font-size: 11px;
    color: var(--ink);
    line-height: 16px;
    border-collapse: collapse;
  }
  .contact td { padding: 0; white-space: nowrap; }
  .contact .label { width: 38px; }

  .site {
    position: absolute;
    left: 0; right: 0;
    bottom: 32px;
    text-align: center;
    font-family: var(--serif);
    font-size: 15px;
    letter-spacing: 2.5px;
    color: var(--ink);
  }
</style>
</head>
<body>
<main class="sheet">

  <section class="card card--front row-top">
    <svg class="brand-ring" width="100" height="100" viewBox="0 0 100 100" aria-hidden="true">
      <circle cx="50" cy="50" r="44" fill="none" stroke="var(--rose)" stroke-width="5"/>
    </svg>
    <p class="brand-name">Mirela Hartwood</p>
    <div class="accent-rule accent-rule--rose"></div>
    <div class="holder">
      <p class="holder-name">Mirela Hartwood</p>
      <p class="holder-role">Fashion Designer</p>
    </div>
    <table class="contact">
      <tr><td class="label">Phone</td><td>: 0400612347</td></tr>
      <tr><td class="label">Email</td><td>: mirela@mirelahartwood.com</td></tr>
      <tr><td class="label">Web</td><td>: www.mirelahartwood.com</td></tr>
    </table>
  </section>

  <section class="card card--back card--back-rose row-top">
    <svg class="brand-ring" width="128" height="128" viewBox="0 0 128 128" aria-hidden="true">
      <circle cx="64" cy="64" r="56" fill="none" stroke="#ffffff" stroke-width="7"/>
    </svg>
    <p class="brand-name">Mirela Hartwood</p>
    <p class="site">WWW.MIRELAHARTWOOD.COM</p>
  </section>

  <section class="card card--front row-bottom">
    <svg class="brand-ring" width="100" height="100" viewBox="0 0 100 100" aria-hidden="true">
      <circle cx="50" cy="50" r="44" fill="none" stroke="var(--sun)" stroke-width="5"/>
    </svg>
    <p class="brand-name">Mirela Hartwood</p>
    <div class="accent-rule accent-rule--sun"></div>
    <div class="holder">
      <p class="holder-name">Mirela Hartwood</p>
      <p class="holder-role">Fashion Designer</p>
    </div>
    <table class="contact">
      <tr><td class="label">Phone</td><td>: 0400612347</td></tr>
      <tr><td class="label">Email</td><td>: mirela@mirelahartwood.com</td></tr>
      <tr><td class="label">Web</td><td>: www.mirelahartwood.com</td></tr>
    </table>
  </section>

  <section class="card card--back card--back-sun row-bottom">
    <svg class="brand-ring" width="128" height="128" viewBox="0 0 128 128" aria-hidden="true">
      <circle cx="64" cy="64" r="56" fill="none" stroke="#ffffff" stroke-width="7"/>
    </svg>
    <p class="brand-name">Mirela Hartwood</p>
    <p class="site">WWW.MIRELAHARTWOOD.COM</p>
  </section>

</main>
</body>
</html>
```